BPL its me again- No TIME

I am a weight loss consultant who my target audience now is staff- teachers at work.

I am Bright Path Living and I have partner up with the program Vital Kickoff. I am selling my services but it will be attached to his brochure which I attached to show you.

This flyer will be given to teachers while at work or left on the staff room lunch table.

Please make it short, snappy and fun.
Why lose weight at work? People are time poor

points:-
- Mobile weight loss consultant who comes to you at work
before/after school or lunch break.
-20 minute private 1 on 1 consultations
-limited spots (3 per hour)
-no contract
-10 years experience

If possible I would like it at work flyer for different companies as well like banks but teachers/schools are my main target.

Like the picture with the teacher in front of the board but can remove the heart if possible
Thank you

i will brochure soon to show you

Target Market(s)

people at work- during lunch breaks or before and after
First is school teachers then other companies.
Females are the majority of clients

Industry/Entity Type

Teacher

Requirements
Must have
• leave it up to you just want to grab staff's attention.
Should not have
• please never use the word "diet" its a healthy lifestyle.

```html
<!DOCTYPE html>
<html lang="en">
<head>
<meta charset="utf-8">
<title>Why lose weight at work? – Bright Path Living</title>
<link rel="stylesheet" href="https://fonts.googleapis.com/css2?family=Questrial&display=swap">
<style>
  :root {
    --red: #d8283f;
    --white: #ffffff;
    --blue: #1f5fa3;
    --blue-deep: #12437f;
    --green: #8cc63f;
    --lime: #a6ce39;
    --grey-light: #ececec;
    --grey-mid: #d6d6d6;
    --purple: #7b2c8f;
    --purple-deep: #5f1f73;
    --green-dark: #2f7a2f;
    --crimson: #b0223a;
    --teal: #1b6fa8;
    --orange: #f39a1e;
  }
  * { margin: 0; padding: 0; box-sizing: border-box; }
  html, body { width: 847px; height: 1200px; overflow: hidden; background: var(--white); }
  body { font-family: "Questrial", "Century Gothic", sans-serif; }

  .flyer {
    position: relative;
    width: 847px;
    height: 1200px;
    overflow: hidden;
    isolation: isolate;
    background: linear-gradient(160deg, var(--white) 0%, var(--grey-light) 45%, var(--grey-mid) 100%);
  }

  .headline {
    position: absolute;
    top: 16px; left: 62px;
    font-size: 48px;
    font-weight: 400;
    color: var(--red);
    letter-spacing: 0.6px;
    white-space: nowrap;
  }

  .hero-art { position: absolute; top: 0; left: 0; }
  .lower-art { position: absolute; top: 0; left: 0; }

  .hero-title {
    position: absolute;
    top: 102px; right: 20px;
    font-size: 51px;
    font-weight: 400;
    color: var(--white);
    letter-spacing: 0.5px;
    white-space: nowrap;
  }

  .offer {
    position: absolute;
    right: 25px;
    text-align: right;
    color: var(--white);
    white-space: nowrap;
  }
  .offer-mobile { top: 354px; font-size: 40px; }
  .offer-role {
    top: 414px;
    font-size: 33px;
    line-height: 44px;
    color: var(--lime);
    text-transform: uppercase;
  }
  .offer-detail { top: 510px; font-size: 34px; line-height: 44px; }

  .points {
    position: absolute;
    top: 652px; left: 50px;
    list-style: none;
    z-index: 1;
    isolation: isolate;
  }
  .point {
    position: relative;
    font-size: 32px;
    height: 58px;
    line-height: 50px;
    white-space: nowrap;
  }
  .point::before {
    content: "";
    position: absolute;
    left: -20px; top: 18px;
    width: 170px; height: 30px;
    border-radius: 15px;
    opacity: 0.45;
    transform: rotate(-5deg);
    z-index: -1;
  }
  .point--purple { color: var(--purple); }
  .point--purple::before { background: #9a5bb0; }
  .point--green { color: var(--green-dark); }
  .point--green::before { background: var(--green); }
  .point--red { color: var(--crimson); }
  .point--red::before { background: #e86a78; }
  .point--blue { color: var(--teal); }
  .point--blue::before { background: #3fb2e6; }
  .point--orange { color: var(--orange); }
  .point--orange::before { background: #f6d23a; }

  .fitness-still {
    position: absolute;
    left: 0; top: 950px;
    width: 205px; height: 135px;
    background:
      radial-gradient(ellipse 40px 38px at 82px 70px, #8cc63f 0 70%, transparent 100%),
      radial-gradient(ellipse 60px 40px at 30px 40px, #d2496e 0 60%, transparent 100%),
      linear-gradient(90deg, #f4f4f4 0%, #e8e4da 60%, #f4f4f4 100%);
  }

  .partner-badge {
    position: absolute;
    left: 216px; top: 978px;
    width: 128px; height: 92px;
    background: linear-gradient(180deg, var(--white) 0 66%, var(--red) 66% 100%);
    border: 4px solid var(--red);
    border-radius: 9px;
    box-shadow: 0 2px 6px rgba(0,0,0,0.15);
  }

  .brand {
    position: absolute;
    left: 455px; top: 960px;
    display: flex;
    align-items: center;
    gap: 14px;
  }
  .brand-dot {
    width: 54px; height: 54px;
    border-radius: 50%;
    background: var(--purple);
  }
  .brand-name {
    font-size: 36px;
    color: var(--purple);
    white-space: nowrap;
  }

  .booking {
    position: absolute;
    left: 0; bottom: 0;
    width: 847px; height: 110px;
    background: linear-gradient(180deg, #8a3aa0 0%, var(--purple-deep) 100%);
    color: var(--white);
    text-align: center;
    white-space: nowrap;
  }
  .booking-title { padding-top: 10px; font-size: 35px; font-weight: 400; }
  .booking-title strong { font-weight: 400; }
  .booking-contact { margin-top: 8px; font-size: 26px; }
  .booking-contact .sep { margin: 0 12px; }
</style>
</head>
<body>
<main class="flyer">
  <svg class="lower-art" width="847" height="1200" viewBox="0 0 847 1200">
    <polygon points="847,700 847,1090 470,1090" fill="#ffffff" opacity="0.55"/>
    <polygon points="0,940 470,940 470,1090 0,1090" fill="#ffffff" opacity="0.45"/>
  </svg>

  <svg class="hero-art" width="847" height="700" viewBox="0 0 847 700">
    <defs>
      <linearGradient id="photoVertical" x1="0" y1="0" x2="0" y2="1">
        <stop offset="0" stop-color="#7d8994"/>
        <stop offset="0.3" stop-color="#9aa3a6"/>
        <stop offset="0.55" stop-color="#d6d05a"/>
        <stop offset="0.8" stop-color="#c9c34a"/>
        <stop offset="1" stop-color="#3d434a"/>
      </linearGradient>
      <linearGradient id="photoHorizontal" x1="0" y1="0" x2="1" y2="0">
        <stop offset="0" stop-color="#2f3a44" stop-opacity="0.35"/>
        <stop offset="0.35" stop-color="#e04a5a" stop-opacity="0.18"/>
        <stop offset="0.6" stop-color="#ffffff" stop-opacity="0"/>
        <stop offset="1" stop-color="#2f3a44" stop-opacity="0.45"/>
      </linearGradient>
      <linearGradient id="panelTone" x1="0" y1="0" x2="1" y2="1">
        <stop offset="0" stop-color="#2c7bc0"/>
        <stop offset="1" stop-color="#12437f"/>
      </linearGradient>
    </defs>
    <rect x="0" y="88" width="847" height="7" fill="#d8283f"/>
    <g role="img" aria-label="Photo of five smiling staff members in high-visibility vests standing in front of a program banner">
      <polygon points="0,95 847,95 847,680 0,555" fill="url(#photoVertical)"/>
      <polygon points="0,95 847,95 847,680 0,555" fill="url(#photoHorizontal)"/>
    </g>
    <polygon points="847,190 847,680 330,604" fill="url(#panelTone)" opacity="0.95"/>
    <polygon points="847,680 847,700 0,575 0,555" fill="#ffffff" opacity="0.7"/>
    <line x1="0" y1="556" x2="847" y2="681" stroke="#8cc63f" stroke-width="6"/>
  </svg>

  <h1 class="headline">Why lose weight at work?</h1>
  <h2 class="hero-title">People are time poor</h2>

  <p class="offer offer-mobile">Mobile</p>
  <p class="offer offer-role">Weight loss<br>consultant</p>
  <p class="offer offer-detail">who comes to you at work<br>before/after school or<br>lunch break.</p>

  <ul class="points">
    <li class="point point--purple">20 minute private 1 on 1 consultations</li>
    <li class="point point--green">Limited spots (3 per hour)</li>
    <li class="point point--red">No contract</li>
    <li class="point point--blue">10 years experience</li>
    <li class="point point--orange">Convenience</li>
  </ul>

  <div class="fitness-still" role="img" aria-label="Photo of pink dumbbells, a green apple and a measuring tape"></div>
  <div class="partner-badge" role="img" aria-label="Vital Kickoff official partner badge"></div>

  <div class="brand">
    <span class="brand-dot"></span>
    <span class="brand-name">Bright Path Living</span>
  </div>

  <footer class="booking">
    <p class="booking-title">To book your <strong>FREE Consultation</strong></p>
    <p class="booking-contact">Call Clara - 0400 123 456<span class="sep">|</span>clara@brightpathliving.com.au</p>
  </footer>
</main>
</body>
</html>
```